Course Graduation Certificate

This project is not for a flyer but instead for the creation of a course graduation certificate. The final certificate needs to include the Marlowe Summit Aviation Academy logo and the text stating as follows:
Certifies that ___________________________ has satisfactorily completed the course of _______________________________ on ________________________________
I would also like to include some type of gold seal of completion as well as a place to sign my name and credentials at the bottom of the certificate
I have included the Marlowe Summit Aviation Academy logo as well as three other certificate examples for you to work from.
Target Market(s)
Students completing a certification course and receiving a certificate
Look and feel

```html
<!DOCTYPE html>
<html lang="en">
<head>
<meta charset="utf-8">
<title>Course Graduation Certificate</title>
<link rel="stylesheet" href="https://fonts.googleapis.com/css2?family=Rye&family=Alegreya+Sans:wght@500&family=Fondamento&family=Oswald:wght@400;500&display=swap">
<style>
  :root {
    --blue-deep: #0057a8;
    --blue-mid: #0779ba;
    --blue-soft: rgba(7, 121, 186, 0.16);
    --frame-blue: #0c76bd;
    --title-blue: #0a56aa;
    --ink: #111111;
    --gold-light: #e9cf8e;
    --gold-dark: #b8944c;
    --paper: #ffffff;
  }
  html, body { margin: 0; padding: 0; overflow: hidden; background: var(--paper); }
  .certificate {
    position: relative;
    width: 1200px;
    height: 927px;
    background: var(--paper);
    overflow: hidden;
  }
  .decor { position: absolute; inset: 0; }
  .title {
    position: absolute; left: 0; width: 1200px; top: 110px;
    text-align: center; margin: 0;
    font-family: "Rye", serif; font-weight: 400;
    font-size: 72px; line-height: 1; letter-spacing: 1px;
    color: var(--title-blue);
  }
  .subtitle {
    position: absolute; left: 492px; top: 195px; margin: 0;
    font-family: "Alegreya Sans", sans-serif; font-weight: 500;
    font-size: 38px; line-height: 1; color: var(--title-blue);
  }
  .flight-art {
    position: absolute; left: 925px; top: 95px; width: 190px; height: 160px;
    border-radius: 50%;
    background: radial-gradient(ellipse at 40% 40%, var(--blue-soft) 0%, rgba(7, 121, 186, 0) 70%);
  }
  .script {
    position: absolute; margin: 0;
    font-family: "Fondamento", cursive; color: var(--ink); line-height: 1;
  }
  .certifies { left: 0; width: 1206px; top: 293px; text-align: center; font-size: 25px; }
  .completed { left: 0; width: 1202px; top: 438px; text-align: center; font-size: 26px; }
  .on { left: 323px; top: 588px; font-size: 30px; }
  .fill-line { position: absolute; height: 1px; background: var(--ink); }
  .line-name { left: 173px; width: 855px; top: 392px; }
  .line-course { left: 173px; width: 855px; top: 535px; }
  .line-date { left: 397px; width: 480px; top: 620px; }
  .line-sign { left: 761px; width: 298px; top: 727px; }
  .seal {
    position: absolute; left: 139px; top: 659px; width: 136px; height: 136px;
    border-radius: 50%;
    background: radial-gradient(circle, var(--gold-light) 55%, var(--gold-dark) 100%);
  }
  .motto {
    position: absolute; left: 86px; width: 240px; top: 805px; margin: 0;
    text-align: center; font-family: "Oswald", sans-serif; font-weight: 400;
    font-size: 14px; line-height: 19px; color: var(--ink);
  }
  .academy-name {
    position: absolute; left: 425px; width: 270px; top: 776px; margin: 0;
    text-align: center; font-family: "Oswald", sans-serif; font-weight: 500;
    font-size: 21px; line-height: 26px; color: var(--title-blue);
    text-transform: uppercase; letter-spacing: 1px;
  }
  .signatory {
    position: absolute; left: 760px; width: 300px; top: 752px; margin: 0;
    text-align: center; font-family: "Oswald", sans-serif; font-weight: 500;
    font-size: 22px; line-height: 1; color: var(--ink);
  }
</style>
</head>
<body>
<main class="certificate">
  <svg class="decor" width="1200" height="927" viewBox="0 0 1200 927" aria-hidden="true">
    <g stroke="var(--frame-blue)" stroke-width="3" fill="none">
      <line x1="330" y1="54" x2="1200" y2="54"/>
      <line x1="1147" y1="0" x2="1147" y2="927"/>
      <line x1="55" y1="200" x2="55" y2="927"/>
      <line x1="0" y1="879" x2="1000" y2="879"/>
    </g>
    <path d="M0 0 H380 C350 60 300 110 210 130 C130 150 60 190 0 285 Z" fill="var(--blue-mid)"/>
    <path d="M0 0 H380 C340 70 270 95 200 100 C110 110 40 140 0 180 Z" fill="var(--blue-deep)"/>
    <path d="M1200 687 C1160 740 1080 790 1000 810 C920 830 870 880 846 927 H1200 Z" fill="var(--blue-mid)"/>
    <path d="M1200 780 C1140 820 1060 835 1000 845 C930 857 890 890 870 927 H1200 Z" fill="var(--blue-deep)"/>
  </svg>

  <h1 class="title">CERTIFICATE</h1>
  <p class="subtitle">of Graduation</p>
  <div class="flight-art" role="img" aria-label="Airplane illustration with dashed flight path"></div>

  <p class="script certifies">Certifies That</p>
  <div class="fill-line line-name"></div>
  <p class="script completed">has satisfactorily completed the course of</p>
  <div class="fill-line line-course"></div>
  <p class="script on">on</p>
  <div class="fill-line line-date"></div>

  <div class="seal" role="img" aria-label="Gold seal of completion"></div>
  <p class="motto">The best Safety device in any aircraft<br>is a well-trained pilot</p>

  <p class="academy-name">Marlowe Summit Aviation Academy</p>

  <div class="fill-line line-sign"></div>
  <p class="signatory">Authorized Signatory</p>
</main>
</body>
</html>
```